A poster for international internet marketing exhibition event

We need a poster design for a B2B exhibition event. Main purpose of the poster is to promote the company brand and showcase our services.

Main Tag line 1: Improve Web Visibility
Main Tag line 2: Get Laser Targeted Traffic To Your Website

Through the poster, we hope to convey a fun and professional company culture.
We would like to see designs that use the colour of sky blue and white (to be in lined with our company website).

Some important information:
Services Offer: Search Engine Optimization, Search Engine Marketing, Social Media Marketing, Video Marketing, Reputation Management, Ranking Maintenance, Web Design & Development
Core Business: Search Engine Optimization

Company Name: BrimtideRank Pte Ltd
Website: http://www.brimtiderank.com.sg
Resolution: 300 dpi (minimum)
Dimension: 85cm (Width) x 200 cm (height)
Preferably in Photoshop format (.psd)

Target Market(s)

Corporate Customers. Target market will usually be business owners and marketing professionals.

Industry/Entity Type

Internet

Requirements
Must have
• The poster must show all the services that are offered. Does not require to provide description for each service.
The poster also must show company logo in prominent position.

```html
<!DOCTYPE html>
<html lang="en">
<head>
<meta charset="utf-8">
<title>BrimtideRank – Exhibition Banner</title>
<link rel="stylesheet" href="https://fonts.googleapis.com/css2?family=Play:wght@400;700&family=PT+Sans:wght@400;700&display=swap">
<style>
  :root {
    --page: #ffffff;
    --sky-top: #64bdd0;
    --sky-mid: #4aa9c0;
    --sky-low: #5cb8ca;
    --cloud: rgba(225, 240, 246, 0.55);
    --badge: #2e8fae;
    --badge-text: #dfeaf0;
    --ink: #111417;
    --brand: #3a4350;
  }
  * { box-sizing: border-box; margin: 0; padding: 0; }
  html, body {
    width: 900px; height: 1200px; overflow: hidden;
    background: var(--page);
  }
  .banner {
    position: absolute; left: 212px; top: 40px;
    width: 476px; height: 1120px; overflow: hidden;
    color: var(--ink);
    font-family: "Play", sans-serif;
    text-align: center;
  }
  .banner__backdrop {
    position: absolute; inset: 0;
    background:
      radial-gradient(ellipse 60% 18% at 50% 9%, var(--cloud), transparent 70%),
      radial-gradient(ellipse 70% 22% at 45% 52%, rgba(210, 228, 236, 0.6), transparent 70%),
      radial-gradient(ellipse 60% 20% at 55% 90%, rgba(200, 230, 238, 0.4), transparent 70%),
      linear-gradient(180deg, var(--sky-top) 0%, var(--sky-mid) 45%, var(--sky-low) 100%);
  }
  .brand { position: absolute; left: 0; right: 0; top: 56px; }
  .brand__name {
    font-family: "PT Sans", sans-serif; font-weight: 400;
    font-size: 38px; letter-spacing: 0.5px; color: var(--brand); line-height: 1;
  }
  .headline-badge {
    position: absolute; left: 62px; top: 320px;
    width: 352px; height: 352px; border-radius: 50%;
    background: var(--badge);
    display: flex; flex-direction: column; justify-content: center; align-items: center;
  }
  .headline-badge__line {
    font-family: "Play", sans-serif; font-weight: 700;
    font-size: 60px; line-height: 68px; letter-spacing: 2px;
    color: var(--badge-text);
  }
  .subheadline {
    position: absolute; left: 0; right: 0; top: 692px;
    font-family: "PT Sans", sans-serif; font-weight: 700;
    font-size: 31px; line-height: 46px;
  }
  .services { position: absolute; left: 0; right: 0; top: 806px; }
  .section-title {
    font-family: "Play", sans-serif; font-weight: 700;
    font-size: 26px; line-height: 30px; letter-spacing: 1px;
  }
  .services__list { list-style: none; margin-top: 2px; }
  .services__item {
    font-weight: 700; font-size: 15px; line-height: 17px; letter-spacing: 0.5px;
  }
  .core { position: absolute; left: 0; right: 0; top: 994px; }
  .core__item { font-weight: 700; font-size: 15px; line-height: 18px; letter-spacing: 0.5px; }
  .website {
    position: absolute; left: 0; right: 0; top: 1082px;
    font-weight: 700; font-size: 13px; letter-spacing: 1px;
  }
</style>
</head>
<body>
  <main class="banner">
    <div class="banner__backdrop" role="img" aria-label="Sky-blue backdrop of soft clouds overlaid with a faint network of connected dots"></div>

    <header class="brand">
      <div class="brand__name">BRIMTIDERANK</div>
    </header>

    <h1 class="headline-badge">
      <span class="headline-badge__line">improve</span>
      <span class="headline-badge__line">web</span>
      <span class="headline-badge__line">visibility</span>
    </h1>

    <h2 class="subheadline">Get Laser Targeted<br>Traffic To Your Website</h2>

    <section class="services">
      <h3 class="section-title">services offer</h3>
      <ul class="services__list">
        <li class="services__item">search engine optimization</li>
        <li class="services__item">search engine marketing</li>
        <li class="services__item">social media marketing</li>
        <li class="services__item">video marketing</li>
        <li class="services__item">reputation management</li>
        <li class="services__item">ranking maintenance</li>
        <li class="services__item">web design &amp; development</li>
      </ul>
    </section>

    <section class="core">
      <h3 class="section-title">core business</h3>
      <p class="core__item">search engine optimization</p>
    </section>

    <p class="website">www.brimtiderank.com.sg</p>
  </main>
</body>
</html>
```